Verdant Solutions Business Card

want the back of card to be blue- with the logo in the center
front of card- info plus logo (info being mailing address, email address, and website address )
4 different names with titles to have on cards
1) Dalton Mirsky - Owner
2) Brenda Tolvin- Customer Relationship Specialist
3) Henri Kastner- Vice President of Sales
4) Wade Dunmor- Chief Technology Officer

Target Market(s)

tech company in the government/probation office industry

Industry/Entity Type

Government Office

Contact Information for Business Card

1) Dalton Mirsky - Owner

Colors
0355a3
ffffff

Requirements
Must have
• back side should be blue, with the logo placed in the center
• front side needs to include both the logo, as well as company info (info should include website address, email address, and mailing address)

```html
<!DOCTYPE html>
<html lang="en">
<head>
<meta charset="utf-8">
<title>Verdant Solutions Business Card</title>
<link rel="stylesheet" href="https://fonts.googleapis.com/css2?family=Cinzel:wght@600&family=Open+Sans:wght@400&display=swap">
<style>
  :root {
    --brand-blue: #0355a3;
    --white: #ffffff;
    --band-grey: #8e8f92;
    --text-grey: #7d7e81;
    --divider-grey: #9a9b9e;
    --page-bg: #e4e5e7;
  }
  * { box-sizing: border-box; margin: 0; padding: 0; }
  html, body { width: 1200px; height: 895px; overflow: hidden; }
  body {
    position: relative;
    background: var(--page-bg);
    font-family: "Open Sans", sans-serif;
  }
  .card {
    position: absolute;
    width: 620px;
    height: 354px;
    border-radius: 2px;
    box-shadow: 0 6px 18px rgba(0,0,0,0.18);
    overflow: hidden;
  }
  /* Back side */
  .card-back {
    left: 50px; top: 50px;
    background: var(--brand-blue);
    color: var(--white);
  }
  .card-back .wordmark {
    position: absolute;
    left: 0; right: 0; top: 118px;
    text-align: center;
    font-family: "Cinzel", serif;
    font-weight: 600;
    color: var(--white);
    line-height: 1.05;
  }
  .card-back .wordmark .line-main { display: block; font-size: 56px; letter-spacing: 1px; }
  .card-back .wordmark .line-sub { display: block; font-size: 22px; letter-spacing: 11px; margin-top: 4px; }
  .card-back .web {
    position: absolute;
    left: 0; right: 0; bottom: 44px;
    text-align: center;
    font-family: "Cinzel", serif;
    font-weight: 600;
    font-size: 14px;
    letter-spacing: 1px;
  }
  /* Front side */
  .card-front {
    left: 530px; top: 490px;
    background: var(--white);
  }
  .card-front .wordmark {
    position: absolute;
    left: 250px; top: 36px;
    font-family: "Cinzel", serif;
    font-weight: 600;
    color: var(--brand-blue);
    line-height: 1.05;
  }
  .card-front .wordmark .line-main { display: block; font-size: 44px; letter-spacing: 1px; }
  .card-front .wordmark .line-sub { display: block; font-size: 17px; letter-spacing: 9px; margin-top: 3px; }
  .person {
    position: absolute;
    right: 290px; top: 172px;
    text-align: right;
  }
  .person .name {
    font-family: "Cinzel", serif;
    font-weight: 600;
    font-size: 28px;
    line-height: 1.2;
    color: var(--brand-blue);
    white-space: nowrap;
  }
  .person .title {
    font-size: 15px;
    color: var(--text-grey);
    margin-top: 2px;
  }
  .divider {
    position: absolute;
    left: 345px; top: 160px;
    width: 1px; height: 80px;
    background: var(--divider-grey);
  }
  .contact {
    position: absolute;
    left: 362px; top: 161px;
    list-style: none;
    font-size: 14px;
    color: var(--text-grey);
  }
  .contact li {
    display: flex;
    align-items: center;
    gap: 9px;
    height: 26px;
    white-space: nowrap;
  }
  .contact svg { width: 13px; height: 13px; fill: var(--brand-blue); flex: none; }
  .address-band {
    position: absolute;
    left: 0; right: 0; bottom: 38px;
    height: 38px;
    background: var(--band-grey);
    color: var(--white);
    font-size: 15px;
    display: flex;
    align-items: center;
    justify-content: center;
    letter-spacing: 0.3px;
  }
  .base-band {
    position: absolute;
    left: 0; right: 0; bottom: 0;
    height: 22px;
    background: var(--band-grey);
  }
</style>
</head>
<body>
  <section class="card card-back" aria-label="Card back">
    <div class="wordmark">
      <span class="line-main">VERDANT</span>
      <span class="line-sub">SOLUTIONS</span>
    </div>
    <p class="web">www.verdantsolutions.com</p>
  </section>

  <section class="card card-front" aria-label="Card front">
    <div class="wordmark">
      <span class="line-main">VERDANT</span>
      <span class="line-sub">SOLUTIONS</span>
    </div>

    <div class="person">
      <p class="name">DALTON MIRSKY</p>
      <p class="title">Owner</p>
    </div>

    <div class="divider"></div>

    <ul class="contact">
      <li>
        <svg viewBox="0 0 24 24" aria-hidden="true"><path d="M6.6 10.8a15.1 15.1 0 0 0 6.6 6.6l2.2-2.2a1 1 0 0 1 1-.25 11.4 11.4 0 0 0 3.6.57 1 1 0 0 1 1 1V20a1 1 0 0 1-1 1A17 17 0 0 1 3 4a1 1 0 0 1 1-1h3.5a1 1 0 0 1 1 1c0 1.25.2 2.45.57 3.57a1 1 0 0 1-.25 1z"/></svg>
        <span>000 000 0000</span>
      </li>
      <li>
        <svg viewBox="0 0 24 24" aria-hidden="true"><path d="M2 5h20v14H2z M2 5l10 8 10-8" /></svg>
        <span>dalton@verdantsolutions.com</span>
      </li>
      <li>
        <svg viewBox="0 0 24 24" aria-hidden="true"><circle cx="12" cy="12" r="10"/><path d="M2 12h20M12 2c3 3 3 17 0 20M12 2c-3 3-3 17 0 20" stroke="#ffffff" stroke-width="1.5" fill="none"/></svg>
        <span>www.verdantsolutions.com</span>
      </li>
    </ul>

    <div class="address-band">48 Harrow Lane, Suite B, Leeds, UK 204517</div>
    <div class="base-band"></div>
  </section>
</body>
</html>
```